Hi Corinna, we need our wine labels produced for this year's vintage with a few changes. We would like to keep the integrity of the current label for the H and want the blue and gold to remain in the design. However we would like to include an image of a tree and our dogs.

```html
<!DOCTYPE html>
<html lang="en">
<head>
<meta charset="utf-8">
<title>Marlowe Estate – Tiller's Paddock Pinot Noir Label</title>
<link rel="stylesheet" href="https://fonts.googleapis.com/css2?family=Arimo:wght@400;700&family=EB+Garamond:ital,wght@1,400&display=swap">
<style>
  :root {
    --backdrop: #e9ecee;
    --label: #ffffff;
    --navy: #1f2370;
    --gold: #7d6a2c;
    --gold-light: #a48f48;
    --gold-mist: rgba(125, 106, 44, 0.12);
    --ink: #111111;
  }
  html, body {
    margin: 0;
    padding: 0;
    width: 1200px;
    height: 923px;
    overflow: hidden;
    background: var(--backdrop);
  }
  .label {
    position: absolute;
    left: 247px;
    top: 140px;
    width: 703px;
    height: 642px;
    background: var(--label);
    font-family: "Arimo", Arial, sans-serif;
    overflow: hidden;
  }
  .pattern-top {
    position: absolute;
    left: 0; top: 0;
    width: 703px;
    height: 112px;
  }
  .estate-mark {
    position: absolute;
    left: 0; top: 74px;
    width: 703px;
    text-align: center;
    font-weight: 700;
    font-size: 16px;
    line-height: 1;
    color: var(--gold);
  }
  .estate-name {
    position: absolute;
    left: 0; top: 121px;
    width: 703px;
    text-align: center;
    margin: 0;
    font-weight: 700;
    font-size: 44px;
    line-height: 1;
    color: var(--gold);
  }
  .vineyard-name {
    position: absolute;
    left: 0; top: 166px;
    width: 703px;
    text-align: center;
    margin: 0;
    font-family: "EB Garamond", Georgia, serif;
    font-style: italic;
    font-weight: 400;
    font-size: 46px;
    line-height: 1.1;
    color: var(--navy);
  }
  .tree-illustration {
    position: absolute;
    left: 228px; top: 216px;
    width: 254px; height: 304px;
    background: radial-gradient(ellipse at 50% 50%, var(--gold-light) 0%, var(--gold) 45%, var(--gold-mist) 85%, var(--label) 100%);
  }
  .variety, .vintage, .region {
    position: absolute;
    left: 0;
    width: 703px;
    text-align: center;
    margin: 0;
    font-weight: 700;
    color: var(--ink);
    line-height: 1;
  }
  .variety { top: 526px; font-size: 24px; }
  .vintage { top: 556px; font-size: 24px; }
  .region  { top: 587px; font-size: 18.5px; }
  .fine-print {
    position: absolute;
    margin: 0;
    color: var(--ink);
    line-height: 1;
  }
  .preservative { left: 9px; top: 591px; font-size: 14px; }
  .volume { right: 12px; top: 567px; font-size: 16px; text-align: right; }
  .alcohol { right: 12px; top: 589px; font-size: 16px; text-align: right; }
  .pattern-bottom {
    position: absolute;
    left: 0; top: 609px;
    width: 703px; height: 33px;
    background: var(--gold);
  }
</style>
</head>
<body>
  <main class="label">
    <svg class="pattern-top" viewBox="0 0 703 112" role="img" aria-label="Navy chevron pattern band with gold zigzag edge">
      <rect x="0" y="0" width="703" height="91" fill="var(--navy)"/>
      <rect x="0" y="91" width="703" height="19" fill="var(--gold)"/>
      <circle cx="352" cy="110" r="66" fill="var(--label)"/>
    </svg>
    <div class="estate-mark">Marlowe</div>

    <h1 class="estate-name">MARLOWE ESTATE</h1>
    <h2 class="vineyard-name">Tiller’s Paddock</h2>

    <div class="tree-illustration" role="img" aria-label="Gold brush illustration of a tall pine tree with two small dogs sitting at its base"></div>

    <p class="variety">PINOT NOIR</p>
    <p class="vintage">2019</p>
    <p class="region">MORNINGTON PENINSULA</p>

    <p class="fine-print preservative">Preservative 220 added</p>
    <p class="fine-print volume">750 ml</p>
    <p class="fine-print alcohol">ALC/VOL 14.8%</p>

    <div class="pattern-bottom" role="img" aria-label="Gold chevron pattern band"></div>
  </main>
</body>
</html>
```